Venture Keeper's Lanternbook

We need a cover design for a printed paperback book 8.5 inches by 11 inches. The book is a self-driven business planning process for people who wish to start or buy a business, be their own boss, entrepreneurs, small and home-based business owners. We hope for a design that is fun, with a treasure map flavor.

```html
<!DOCTYPE html>
<html lang="en">
<head>
<meta charset="utf-8">
<title>Venture Keeper's Lanternbook — Book Cover</title>
<link rel="stylesheet" href="https://fonts.googleapis.com/css2?family=Josefin+Sans:wght@600;700&display=swap">
<style>
  :root {
    --paper: #fdfdfd;
    --ink: #1c1c1c;
    --bar-top: #161616;
    --bar-bottom: #464646;
    --accent: #e8273f;
    --figure: #111111;
  }
  html, body {
    margin: 0;
    padding: 0;
    overflow: hidden;
    background: var(--paper);
  }
  .cover {
    position: relative;
    width: 900px;
    height: 1200px;
    background: var(--paper);
    overflow: hidden;
  }
  .cover-title {
    position: absolute;
    top: 58px;
    left: 0;
    width: 100%;
    margin: 0;
    text-align: center;
    font-family: "Josefin Sans", "Century Gothic", sans-serif;
    font-weight: 600;
    font-size: 76px;
    line-height: 114px;
    letter-spacing: 1px;
    text-transform: uppercase;
    color: var(--ink);
  }
  .cover-title span { display: block; }
  .growth-chart {
    position: absolute;
    left: 0;
    top: 0;
    width: 900px;
    height: 1200px;
  }
  .cover-author {
    position: absolute;
    top: 1112px;
    left: 0;
    width: 100%;
    margin: 0;
    text-align: center;
    font-family: "Josefin Sans", "Century Gothic", sans-serif;
    font-weight: 700;
    font-size: 25px;
    letter-spacing: 1.5px;
    text-transform: uppercase;
    color: var(--ink);
  }
</style>
</head>
<body>
<main class="cover">
  <h1 class="cover-title"><span>Venture Keeper's</span><span>Lanternbook</span></h1>

  <svg class="growth-chart" viewBox="0 0 900 1200" aria-hidden="false">
    <defs>
      <linearGradient id="bar-shade" x1="0" y1="0" x2="0" y2="1">
        <stop offset="0" stop-color="var(--bar-top)" style="stop-color: var(--bar-top)"/>
        <stop offset="1" stop-color="var(--bar-bottom)" style="stop-color: var(--bar-bottom)"/>
      </linearGradient>
    </defs>

    <g class="chart-axes" stroke="var(--ink)" style="stroke: var(--ink)" stroke-width="3" fill="none">
      <line x1="177" y1="528" x2="177" y2="774"/>
      <line x1="175" y1="773" x2="728" y2="773"/>
    </g>
    <g class="axis-arrows" style="fill: var(--ink)">
      <polygon points="177,520 169,538 185,538"/>
      <polygon points="735,773 716,765 716,781"/>
    </g>

    <g class="chart-bars" fill="url(#bar-shade)">
      <rect x="205" y="745" width="34" height="27"/>
      <rect x="260" y="732" width="34" height="40"/>
      <rect x="316" y="717" width="34" height="55"/>
      <rect x="372" y="706" width="34" height="66"/>
      <rect x="428" y="675" width="34" height="97"/>
      <rect x="484" y="637" width="34" height="135"/>
      <rect x="540" y="616" width="34" height="156"/>
      <rect x="595" y="588" width="34" height="184"/>
    </g>
    <rect class="chart-bar-peak" x="651" y="542" width="34" height="230" style="fill: var(--accent)"/>

    <g class="climber-figures" style="fill: var(--figure)">
      <rect role="img" aria-label="Small silhouette of a businessperson standing on a bar" x="218" y="716" width="8" height="29"/>
      <rect role="img" aria-label="Small silhouette of a businessperson standing on a bar" x="273" y="703" width="8" height="29"/>
      <rect role="img" aria-label="Small silhouette of a businessperson standing on a bar" x="329" y="688" width="8" height="29"/>
      <rect role="img" aria-label="Small silhouette of a businessperson standing on a bar" x="385" y="672" width="8" height="34"/>
      <rect role="img" aria-label="Small silhouette of a businessperson standing on a bar" x="441" y="644" width="8" height="31"/>
      <rect role="img" aria-label="Small silhouette of a businessperson shrugging on a bar" x="494" y="607" width="14" height="30"/>
      <rect role="img" aria-label="Small silhouette of a businessperson peering ahead on a bar" x="561" y="584" width="12" height="32"/>
      <rect role="img" aria-label="Small silhouette of a businessperson standing on a bar" x="608" y="552" width="8" height="36"/>
      <rect role="img" aria-label="Small silhouette of a businessperson leaping onto the top bar" x="656" y="516" width="22" height="26"/>
    </g>
  </svg>

  <p class="cover-author">Lee Marchand</p>
</main>
</body>
</html>
```